Full page ad in a magazine

We would like an ad designed to be placed for advertising in magazines, theater playbills, etc. I have attached a copy of some previous ads that were done for us, although they need much improvement and redesigned. We have won "best chiropractor" awards that can be seen on our website home page at harlowspineandjoint.example

```html
<!DOCTYPE html>
<html lang="en">
<head>
<meta charset="utf-8">
<title>Harlow Spine &amp; Joint Center – Magazine Ad</title>
<link href="https://fonts.googleapis.com/css2?family=Montserrat:ital,wght@0,400;0,500;0,600;0,700;1,500&family=Roboto+Slab:wght@400;700;800&display=swap" rel="stylesheet">
<style>
  :root{
    --brand-red:#860000;
    --deep-red:#7a0000;
    --ink:#1f1f1f;
    --charcoal:#262626;
    --paper:#ffffff;
    --backdrop:#d9d9d9;
    --photo-light:#e6e6e6;
    --photo-mid:#a9a9a9;
    --photo-dark:#4a4a4a;
  }
  *{margin:0;padding:0;box-sizing:border-box}
  html,body{width:698px;height:1200px;overflow:hidden;background:var(--backdrop)}
  body{font-family:"Montserrat",Arial,sans-serif;color:var(--ink)}
  .ad{position:absolute;left:0;top:127px;width:698px;height:946px;background:var(--paper);overflow:hidden;box-shadow:0 4px 14px rgba(0,0,0,.25)}
  .abs{position:absolute}

  /* header */
  .header{left:0;top:0;width:698px;height:123px}
  .brand-name{left:28px;top:40px;font-family:"Roboto Slab",Georgia,serif;font-weight:700;font-size:24px;line-height:1.1;color:var(--brand-red);display:flex;align-items:center;gap:10px}
  .brand-name .mark{width:22px;height:22px;background:var(--brand-red);flex:none}
  .contact{right:29px;top:34px;text-align:right;color:#fff;font-size:15px;line-height:25px;font-weight:500}
  .contact svg{vertical-align:-2px;margin-left:5px}

  /* hero */
  .hero-photo{left:0;top:123px;width:698px;height:250px;background:linear-gradient(90deg,#5a5a5a 0%,#9c9c9c 35%,#d8d8d8 60%,#f2f2f2 100%)}
  .hero-rule{left:0;top:373px;width:698px;height:7px;background:var(--brand-red)}
  .hero-title{left:380px;top:150px;width:289px;text-align:right;font-family:"Roboto Slab",Georgia,serif;font-weight:800;font-size:52px;line-height:1;color:var(--brand-red)}
  .hero-sub{left:380px;top:211px;width:289px;text-align:right;font-size:20px;font-weight:500;color:var(--ink)}
  .hero-line{left:409px;top:250px;width:248px;height:3px;background:var(--brand-red)}
  .hero-note{left:380px;top:261px;width:277px;text-align:right;font-size:16.5px;line-height:20px;font-weight:500}

  /* info */
  .info{left:0;top:380px;width:698px;height:311px}
  .location-title{left:29px;top:389px;font-family:"Roboto Slab",Georgia,serif;font-weight:800;font-size:22px;line-height:28px;color:var(--brand-red);white-space:nowrap}
  .address{left:29px;top:443px;color:#fff;font-size:19.5px;line-height:29px;font-weight:500}
  .doctor-name{left:144px;top:585px;font-family:"Roboto Slab",Georgia,serif;font-size:15.5px;line-height:22px;color:#fff;white-space:nowrap}
  .phone-big{right:29px;top:407px;font-family:"Roboto Slab",Georgia,serif;font-weight:800;font-size:38px;line-height:1;color:var(--ink);white-space:nowrap}
  .hours{left:350px;top:446px;width:310px;text-align:center;color:#fff;font-size:18px;font-weight:600;line-height:30px;white-space:nowrap}

  /* bottom */
  .bottom{left:0;top:688px;width:698px;height:258px}
  .voted{left:0;top:704px;width:212px;text-align:center;color:#fff;font-weight:700;font-size:33px;line-height:44px}
  .best{left:0;top:752px;width:212px;text-align:center;font-family:"Roboto Slab",Georgia,serif;font-weight:800;font-size:13.5px;color:var(--brand-red);line-height:22px;white-space:nowrap}
  .region{left:29px;top:906px;color:#fff;font-style:italic;font-weight:500;font-size:14.5px;line-height:20px}
  .pain-title{left:236px;top:709px;font-family:"Roboto Slab",Georgia,serif;font-weight:800;font-size:36px;line-height:40px;color:var(--brand-red);white-space:nowrap}
  .services{left:238px;top:751px;font-weight:700;font-size:19px;line-height:24px;color:#2a2a2a;white-space:nowrap}
  .treating{left:238px;top:781px;font-weight:500;font-style:italic;font-size:15px;line-height:20px;color:var(--brand-red)}
  .conditions{top:804px;list-style:none;font-size:17px;line-height:29px;font-weight:500;white-space:nowrap}
  .conditions li::before{content:"\2022\00a0"}
  .conditions.col-a{left:238px}
  .conditions.col-b{left:408px}
  .divider{left:388px;top:809px;width:2px;height:77px;background:var(--ink)}
  .coverage{left:238px;top:896px;font-style:italic;font-weight:500;font-size:13px;line-height:18px;white-space:nowrap}
</style>
</head>
<body>
<main class="ad">

  <!-- header -->
  <svg class="abs header" width="698" height="123" viewBox="0 0 698 123">
    <polygon points="388,0 698,0 698,123 354,123" fill="var(--brand-red)"/>
  </svg>
  <div class="abs brand-name"><span class="mark"></span>Harlow Spine &amp; Joint<br>Center</div>
  <div class="abs contact">
    <div>555.204.7731<svg width="12" height="12" viewBox="0 0 24 24"><path d="M6.6 10.8a15 15 0 0 0 6.6 6.6l2.2-2.2c.3-.3.7-.4 1-.2 1.1.4 2.3.6 3.6.6.6 0 1 .4 1 1V20c0 .6-.4 1-1 1A17 17 0 0 1 3 4c0-.6.4-1 1-1h3.5c.6 0 1 .4 1 1 0 1.2.2 2.4.6 3.6.1.3 0 .7-.2 1z" fill="#fff"/></svg></div>
    <div>harlowspineandjoint.example<svg width="12" height="12" viewBox="0 0 24 24"><circle cx="12" cy="12" r="10" fill="none" stroke="#fff" stroke-width="2.5"/><path d="M2 12h20M12 2c3 3 3 17 0 20M12 2c-3 3-3 17 0 20" fill="none" stroke="#fff" stroke-width="2"/></svg></div>
  </div>

  <!-- hero -->
  <div class="abs hero-photo" role="img" aria-label="Black and white photo of two hikers with red backpacks resting on a rocky hilltop under a cloudy sky"></div>
  <div class="abs hero-rule"></div>
  <h1 class="abs hero-title">Advanced</h1>
  <p class="abs hero-sub">Chiropractic Technology</p>
  <div class="abs hero-line"></div>
  <p class="abs hero-note">We use the latest<br>advancements in Chiropractic</p>

  <!-- info -->
  <svg class="abs info" width="698" height="311" viewBox="0 0 698 311">
    <polygon points="0,0 350,0 280,308 0,308" fill="var(--brand-red)"/>
    <polygon points="0,4 343,4 333,51 0,51" fill="var(--paper)"/>
    <polygon points="349,65 669,65 662,97 342,97" fill="var(--charcoal)"/>
    <rect x="0" y="195" width="300" height="2" fill="var(--paper)"/>
    <rect x="0" y="199" width="296" height="34" fill="var(--charcoal)"/>
    <rect x="0" y="235" width="292" height="2" fill="var(--paper)"/>
    <rect x="26" y="152" width="104" height="126" fill="var(--paper)"/>
    <rect x="29" y="155" width="98" height="120" fill="var(--photo-mid)" role="img" aria-label="Portrait photo of the chiropractor"/>
    <g role="img" aria-label="Photo of a smiling senior couple with bicycles">
      <polygon points="296,111 482,111 458,297 262,297" fill="var(--paper)"/>
      <polygon points="300,116 475,116 449,293 266,293" fill="var(--photo-light)" stroke="var(--ink)" stroke-width="2"/>
    </g>
    <g role="img" aria-label="Photo of a swimmer in a red cap gliding through water">
      <polygon points="492,116 671,116 630,293 458,293" fill="var(--photo-dark)" stroke="var(--brand-red)" stroke-width="2"/>
    </g>
  </svg>
  <h2 class="abs location-title">NORTHGATE LOCATION</h2>
  <p class="abs address">1120 Larkfield Ave., #310<br>Harlow, VA 23000</p>
  <p class="abs doctor-name">Martin Avery, DC</p>
  <p class="abs phone-big">555.204.7731</p>
  <p class="abs hours">OPEN MONDAY - SATURDAY</p>

  <!-- bottom -->
  <svg class="abs bottom" width="698" height="258" viewBox="0 0 698 258">
    <rect x="0" y="0" width="698" height="258" fill="var(--paper)"/>
    <rect x="0" y="0" width="698" height="8" fill="var(--charcoal)"/>
    <polygon points="0,0 218,0 212,60 0,60" fill="var(--charcoal)"/>
    <polygon points="0,90 205,90 194,205 0,205" fill="var(--charcoal)"/>
    <polygon points="0,205 194,205 216,226 212,258 0,258" fill="var(--deep-red)"/>
    <rect x="212" y="236" width="486" height="22" fill="var(--charcoal)"/>
    <g role="img" aria-label="Local best-of award badge">
      <rect x="51" y="98" width="113" height="97" fill="#4a72b8"/>
      <rect x="51" y="98" width="113" height="16" fill="#e8703a"/>
      <rect x="51" y="176" width="113" height="19" fill="#3cb6b0"/>
    </g>
    <rect x="536" y="88" width="145" height="170" rx="24" fill="#cfcfcf" role="img" aria-label="Illustration of a man holding his neck and lower back, with red pain highlights"/>
  </svg>
  <p class="abs voted">VOTED</p>
  <p class="abs best">BEST CHIROPRACTOR</p>
  <p class="abs region">Greater Harlow</p>
  <h2 class="abs pain-title">NECK or BACK PAIN?</h2>
  <p class="abs services">CHIROPRACTIC • MASSAGE</p>
  <p class="abs treating">Treating:</p>
  <ul class="abs conditions col-a"><li>BACK PAIN</li><li>NECK PAIN</li><li>HEADACHES</li></ul>
  <div class="abs divider"></div>
  <ul class="abs conditions col-b"><li>JOINT PAIN</li><li>SCIATICA</li><li>FATIGUE</li></ul>
  <p class="abs coverage">Medicare and most Insurance accepted</p>

</main>
</body>
</html>
```